RHS Trifold Brochure

Would like a Trifold Brochure to use for marketing purposes. The company, Reliable Home Solutions is a Handyman Service that offers Residential Home Repairs, Commercial Repairs, Drain Cleaning, Carpet Cleaning and Water Extraction.

I am attaching some pdf files to use as potential verbage and a copy of our business card and logo image file.

Would like to portray a professional image that sets us apart from a "mom and pops" type handyman service.

Industry/Entity Type

Marketing

```html
<!DOCTYPE html>
<html lang="en">
<head>
<meta charset="utf-8">
<title>Reliable Home Solutions – Trifold Brochure</title>
<link rel="stylesheet" href="https://fonts.googleapis.com/css2?family=Roboto:wght@300;400;500;700&display=swap">
<style>
  :root {
    --paper: #fbfbfb;
    --ink-blue: #2b5ba6;
    --bullet-tan: #c7bf9c;
    --ring: #ffffff;
    --carpet-deep: #2f73c9;
    --carpet-mid: #4a8ed8;
    --fiber-light: #bfe6f2;
    --fiber-mid: #7fcbe3;
    --sky: #6aa5dc;
    --lawn: #4d7a34;
    --house: #d9c79c;
    --plumb-light: #e9ecef;
    --plumb-mid: #b9bfc6;
    --bath-light: #d5f0f6;
    --bath-mid: #7fd0e3;
    --tile-deep: #1e4fc4;
    --tile-light: #bfe3f5;
  }
  * { box-sizing: border-box; margin: 0; padding: 0; }
  html, body { width: 1200px; height: 860px; overflow: hidden; background: var(--paper); }
  body { font-family: "Roboto", Arial, sans-serif; color: var(--ink-blue); }

  .brochure { position: relative; width: 1200px; height: 860px; background: var(--paper); }

  .photo { position: absolute; }
  .photo--carpet-top   { left: 0;   top: 0;   width: 398px; height: 285px; background: radial-gradient(circle at 40% 40%, var(--carpet-mid), var(--carpet-deep)); }
  .photo--carpet-fiber { left: 0;   top: 305px; width: 398px; height: 212px; background: linear-gradient(180deg, var(--fiber-light), var(--fiber-mid) 60%, var(--fiber-light)); }
  .photo--house        { left: 440px; top: 0; width: 326px; height: 285px; background: linear-gradient(180deg, var(--sky) 0%, #a9cbe9 35%, var(--house) 55%, var(--lawn) 88%); }
  .photo--plumbing     { left: 440px; top: 305px; width: 326px; height: 212px; background: linear-gradient(135deg, var(--plumb-light), var(--plumb-mid)); }
  .photo--bathroom     { left: 790px; top: 0; width: 410px; height: 285px; background: linear-gradient(135deg, var(--bath-mid), var(--bath-light) 55%, #f4fbfd); }
  .photo--tiles        { left: 790px; top: 305px; width: 410px; height: 212px; background: linear-gradient(135deg, var(--tile-deep), #5aa3e6 50%, var(--tile-light)); }

  .rings { position: absolute; left: 0; top: 0; width: 1200px; height: 860px; pointer-events: none; }

  .badge-title {
    position: absolute; width: 190px; text-align: center;
    font-weight: 300; font-size: 19px; line-height: 23px; color: var(--ink-blue);
    text-transform: uppercase;
  }
  .badge-title--carpet { left: 104px; top: 260px; }
  .badge-title--handyman { left: 508px; top: 238px; }
  .badge-title--handyman .gap { display: block; height: 17px; }
  .badge-title--tile { left: 899px; top: 260px; }

  .panel-copy { position: absolute; font-size: 13.5px; line-height: 16.6px; font-weight: 400; }
  .panel-copy--carpet { left: 106px; top: 534px; width: 234px; text-align: justify; }
  .panel-copy--service { left: 456px; top: 534px; width: 300px; }
  .panel-copy--tile { left: 848px; top: 534px; width: 235px; text-align: justify; }
  .panel-copy p + p { margin-top: 16px; }

  .lead { font-weight: 700; }
  .service-list { list-style: none; margin: 8px 0 14px 42px; color: var(--bullet-tan); }
  .service-list li { line-height: 24px; }
  .service-list li::before { content: "•"; margin-right: 6px; }

  .call-line { position: absolute; left: 100px; top: 768px; font-size: 18px; font-weight: 500; }
  .call-line .phone { margin-left: 6px; }
  .cta { position: absolute; left: 838px; top: 685px; width: 252px; text-align: center; font-size: 17.5px; line-height: 23px; font-weight: 500; }

  .brand-mark { position: absolute; left: 1000px; top: 768px; display: flex; align-items: center; gap: 6px; }
  .brand-mark .dot { width: 10px; height: 10px; background: #1a1a1a; }
  .brand-mark .name { font-size: 13px; font-weight: 700; color: #1a1a1a; }
</style>
</head>
<body>
<main class="brochure">
  <div class="photo photo--carpet-top" role="img" aria-label="Child relaxing on a plush blue carpet"></div>
  <div class="photo photo--carpet-fiber" role="img" aria-label="Close-up of soft light blue carpet fibres"></div>
  <div class="photo photo--house" role="img" aria-label="Two-storey suburban house with lawn under blue sky"></div>
  <div class="photo photo--plumbing" role="img" aria-label="Hands tightening a sink pipe with a wrench"></div>
  <div class="photo photo--bathroom" role="img" aria-label="Bathroom with blue mosaic tile and bathtub"></div>
  <div class="photo photo--tiles" role="img" aria-label="Close-up of blue glass mosaic tiles"></div>

  <svg class="rings" viewBox="0 0 1200 860" aria-hidden="true">
    <g fill="none" stroke="var(--ring)" stroke-width="1.5">
      <circle cx="199" cy="295" r="117"/>
      <circle cx="603" cy="290" r="117"/>
      <circle cx="994" cy="295" r="117"/>
    </g>
    <g fill="var(--ring)">
      <circle cx="199" cy="295" r="97"/>
      <circle cx="603" cy="290" r="97"/>
      <circle cx="994" cy="295" r="97"/>
    </g>
  </svg>

  <h2 class="badge-title badge-title--carpet">Carpet Cleaning<br>&amp; Water<br>Extraction!</h2>
  <h2 class="badge-title badge-title--handyman">Handyman<br>Services!<span class="gap"></span>Drain Cleaning<br>Services!</h2>
  <h2 class="badge-title badge-title--tile">Tile &amp; Grout<br>Cleaning<br>Services!</h2>

  <section class="panel-copy panel-copy--carpet">
    <p>Reliable Home Solutions has your carpet cleaning needs covered. The right equipment and the right experience. Whether it is a routine cleaning or deep stain and odor removal we’ll make sure you’re taken care of. In need of Emergency Water Extraction? We do that too! Give us a Call Today to see what we can do for you...</p>
  </section>

  <section class="panel-copy panel-copy--service">
    <p><span class="lead">We’re here for you!</span><br>
    Have a leaky faucet or a toilet that runs?<br>
    Would you like to hang blinds or repair a hole in the wall?<br>
    How about a fresh coat of paint in the bathroom?</p>
    <ul class="service-list">
      <li>Drain cleaning needs</li>
      <li>Floor Drains</li>
      <li>Tub Drains</li>
      <li>Toilet, Sinks and Main Sewer Lines</li>
    </ul>
    <p>If you don’t know how, don’t have the time or just don’t want to do it yourself give Reliable Home Solutions a call and let us show you what we can do....</p>
  </section>

  <section class="panel-copy panel-copy--tile">
    <p>You mop and you scrub but is that enough? With our tile and grout cleaning equipment you will truly be amazed with the results. Kitchen and bathroom tile, floor or wall and don’t forget the grout.</p>
    <p>Give us a try, you won’t regret it.</p>
  </section>

  <p class="call-line">Call Today!!! <span class="phone">(555) 014 - 2290</span></p>
  <p class="cta">Call Today and schedule your appointment.</p>

  <div class="brand-mark"><span class="dot"></span><span class="name">Reliable Home Solutions</span></div>
</main>
</body>
</html>
```